We are a local Communty Pharmacy wishing to promote and market a specialised Pharmaceutical Service

We would like a design that is professional and enticing ( according to the brief In attached files)
We wish to Market Harbourside Compounding as a specialist side of our business.
We have the expertise a purpose built preparation laboratory.
The main purpose is an Internet presence that entices prospective patients to contact or visit our physical store.

Target Market(s)

Patients Medicos and Veterinary clients

Industry/Entity Type

Pharmacy

Coding

Coded - Design and coding required

Number of Pages Required

1 page

Requirements
Must have
• Clear friendly image
Nice to have
• soft enticing feel
Should not have
• No crass loud unprofessional elements

```html
<!DOCTYPE html>
<html lang="en">
<head>
<meta charset="utf-8">
<title>Harbourside Compounding</title>
<link href="https://fonts.googleapis.com/css2?family=Raleway:wght@400;600;700;800&family=Open+Sans:wght@400;600&display=swap" rel="stylesheet">
<style>
:root{
  --blue:#1ea2e6;
  --red:#f05a4a;
  --ink:#3c4149;
  --muted:#8a9099;
  --light:#f4f5f6;
  --topbar:#2f3338;
  --footer:#3b424c;
  --footer-deep:#2f353d;
  --line:#e2e4e7;
}
*{box-sizing:border-box;margin:0;padding:0}
html,body{width:698px;height:1200px;overflow:hidden;background:#fff}
body{font-family:'Open Sans',sans-serif;color:var(--ink);position:relative}
h1,h2,h3,.brand,.nav a{font-family:'Raleway',sans-serif}

.topbar{height:14px;background:var(--topbar);color:#b9bec5;font-size:6px;display:flex;justify-content:space-between;align-items:center;padding:0 104px}
.header{height:46px;display:flex;align-items:center;justify-content:space-between;padding:0 104px;border-bottom:1px solid var(--line)}
.brand{font-weight:800;font-size:13px;color:var(--blue);letter-spacing:.3px;display:flex;align-items:center;gap:6px}
.brand i{width:9px;height:9px;background:var(--blue);display:block}
.nav{display:flex;height:46px}
.nav a{font-size:6.5px;font-weight:600;color:var(--muted);text-decoration:none;display:flex;align-items:center;padding:0 11px;text-transform:uppercase}
.nav a.active{background:var(--blue);color:#fff}

.hero{position:absolute;top:60px;left:0;width:698px;height:231px;background:linear-gradient(100deg,#e9ecef 0%,#f7f7f5 35%,#d8c9b6 55%,#eef0f1 75%,#dfe4e8 100%)}
.hero-copy{position:absolute;right:104px;top:78px;text-align:right}
.hero-copy h1{font-size:20px;font-weight:800;color:#333;letter-spacing:.2px}
.hero-copy p{font-size:11px;color:var(--blue);font-family:'Raleway',sans-serif;font-weight:600;margin-top:2px}
.btn{display:inline-block;background:var(--red);color:#fff;font-size:10px;padding:6px 13px;text-decoration:none}
.hero-copy .btn{margin-top:10px}

.about{position:absolute;top:291px;left:0;width:698px;height:222px;background:var(--light);text-align:center}
.about h2{font-size:16px;font-weight:800;margin-top:60px}
.about h2 span,.help h2 span{color:var(--blue)}
.about p{font-size:6.5px;color:var(--muted);line-height:1.6;width:410px;margin:10px auto 0}
.about .btn{font-size:7px;padding:4px 10px;margin-top:22px}

.help{position:absolute;top:513px;left:104px;width:490px}
.help h2{font-size:14px;font-weight:800;text-align:center;margin-top:30px}
.tabs{display:flex;margin-top:36px;border-bottom:1px solid var(--line)}
.tab{flex:1;display:flex;align-items:center;gap:6px;font-size:5.5px;color:var(--muted);text-transform:uppercase;padding:14px 0 12px 4px;border-right:1px solid var(--line)}
.tab:last-child{border-right:0}
.tab.active{color:var(--blue);border-bottom:2px solid var(--blue)}
.tab svg{width:10px;height:10px}

.children{display:flex;justify-content:space-between;margin-top:36px}
.children .copy{width:220px}
.children h3{font-size:9px;font-weight:700;text-transform:uppercase}
.children .copy p{font-size:5.5px;color:var(--muted);line-height:1.7;margin-top:16px}
.children .photo{width:236px;height:118px;background:linear-gradient(120deg,#cfe3ef,#e9d7c7 50%,#b9d0dd)}

.testimonial{position:absolute;top:861px;left:0;width:698px;height:117px;background:var(--blue);color:#fff;text-align:center}
.avatar{position:absolute;left:322px;top:-24px;width:54px;height:54px;border-radius:50%;background:#d7dadd;border:3px solid #fff}
.testimonial blockquote{font-size:8.5px;line-height:1.5;width:290px;margin:44px auto 0}
.testimonial cite{display:block;font-style:normal;font-size:7.5px;margin-top:8px}
.testimonial small{display:block;font-size:5px;opacity:.8;margin-top:1px}

.footer{position:absolute;top:989px;left:0;width:698px;height:175px;background:var(--footer);color:#c8ccd2;display:flex;gap:40px;padding:22px 104px 0}
.footer h3{font-size:7px;color:#fff;font-weight:700;margin-bottom:8px}
.footer p{font-size:5.5px;line-height:1.9}
.col-contact{width:120px}
.socials{display:flex;gap:4px;margin-top:5px}
.socials span{width:11px;height:11px;border-radius:50%;background:#59616c;display:block}
.col-news{width:136px}
.signup{display:flex;margin-top:8px}
.signup span{flex:1;height:13px;background:#fff;font-size:5px;color:#999;padding:3px}
.signup b{background:var(--blue);color:#fff;font-size:5.5px;padding:3px 6px}
.map{width:184px;height:112px;background:linear-gradient(135deg,#e6e2d6,#d5dcc7 60%,#c4d6e3)}
.bottombar{position:absolute;top:1164px;left:0;width:698px;height:36px;background:var(--footer-deep);color:#8d949e;font-size:5.5px;padding:10px 104px}
</style>
</head>
<body>
<div class="topbar"><span>Opening Hours: Monday to Saturday 9am to 6pm</span><span>hello@harbourside-rx.example &nbsp;·&nbsp; Call us: 03 5550 1842</span></div>
<header class="header">
  <div class="brand"><i></i>HARBOURSIDE COMPOUNDING</div>
  <nav class="nav"><a class="active">Home</a><a>Compounding Pharmacy</a><a>Services</a><a>News</a><a>Contact Us</a></nav>
</header>

<section class="hero" role="img" aria-label="Pharmacist preparing a compounded medication with mortar, pestle and amber bottles">
  <div class="hero-copy">
    <h1>COMPOUNDING PREPARING</h1>
    <p>Customised Medications for Patients</p>
    <a class="btn">» Read More</a>
  </div>
</section>

<section class="about">
  <h2>WHAT IS <span>COMPOUNDING PHARMACY?</span></h2>
  <p>We prepare medicines to order in our own purpose built laboratory, blending each formula to suit the individual needs of patients, prescribers and animals. Talk to our team about flavours, strengths and forms made just for you.</p>
  <a class="btn">» Read More</a>
</section>

<section class="help">
  <h2>HOW CAN <span>COMPOUNDING</span> HELP?</h2>
  <div class="tabs">
    <div class="tab active"><svg viewBox="0 0 10 10"><circle cx="5" cy="2.5" r="2" fill="currentColor"/><path d="M2 10V6.5Q5 4 8 6.5V10z" fill="currentColor"/></svg>Children</div>
    <div class="tab"><svg viewBox="0 0 10 10"><rect x="1" y="3" width="8" height="6" rx="1" fill="none" stroke="currentColor"/><path d="M3 3V1h4v2" fill="none" stroke="currentColor"/></svg>Difficult to swallow</div>
    <div class="tab"><svg viewBox="0 0 10 10"><circle cx="5" cy="5" r="3.8" fill="none" stroke="currentColor"/><path d="M5 3v4M3 5h4" stroke="currentColor"/></svg>Hormone replacement</div>
    <div class="tab"><svg viewBox="0 0 10 10"><path d="M5 1l1.2 2.6 2.8.3-2.1 1.9.6 2.8L5 7.2 2.5 8.6l.6-2.8L1 3.9l2.8-.3z" fill="none" stroke="currentColor"/></svg>Special dietary requirements</div>
  </div>
  <div class="children">
    <div class="copy">
      <h3>Children</h3>
      <p>We can alter a medicine that is hard to take into a pleasant flavoured liquid, or adjust the dose to suit a small child. Many common medicines are only sold in adult strengths, so we prepare just the right amount for your little one.</p>
    </div>
    <div class="photo" role="img" aria-label="Pharmacist talking with a mother and child at the pharmacy counter"></div>
  </div>
</section>

<section class="testimonial">
  <div class="avatar" role="img" aria-label="Customer portrait"></div>
  <blockquote>Friendly, patient staff and a medicine my daughter will finally take without a fuss. I would gladly recommend this pharmacy to any family.</blockquote>
  <cite>Martin Ellery</cite>
  <small>Parent, local customer</small>
</section>

<footer class="footer">
  <div class="col-contact">
    <h3>Contact Info</h3>
    <p>Ph: 03 5550 1842</p>
    <p>Fax: 03 5550 1843</p>
    <p>Email: hello@harbourside-rx.example</p>
    <h3 style="margin-top:10px">Follow Us</h3>
    <div class="socials"><span></span><span></span><span></span><span></span><span></span></div>
  </div>
  <div class="col-news">
    <h3>Newsletter Signup</h3>
    <p>Join our list for news, health tips and updates from our compounding team.</p>
    <div class="signup"><span>Email address</span><b>Go</b></div>
  </div>
  <div class="map" role="img" aria-label="Map showing the pharmacy location"></div>
</footer>
<div class="bottombar">© Harbourside Compounding. All rights reserved.</div>
</body>
</html>
```